KEV.PRO- Darren Holcombe Fitness- needs a clever business card using the logo, name, info, contact

I need a business card designed for my Online Personal Training company called KEV.PRO, abbreviation for Darren Holcombe Fitness. My company focuses on coaching in personal health and personal growth to unleash your greatest potential. I would like to see designs that use my color scheme of a redish-orange (C:0,M:84,Y:100,K:0), grey, white, black, and my company font is OSWALD. The final design should communicate some aspects of design, health, motivation, growth, in some way. The logo is very important to the company and can be displayed in any of the colors previously mentioned. Must include the company name, my website: www.kev-pro.example , my email: dan@kev-pro.example

Target Market(s)

Personal health, fitness, general public, those who lack knowledge, awareness, and confidence in personal health

Industry/Entity Type

Personal Trainer

Font styles to use
Other font styles liked:
• OSWALD. (Bold, Regular, Light)

Colors
f37122
ffffff
9d9d9d
000000

Requirements
Must have
• Must include the logo, company name, my website: www.kev-pro.example , my email: dan@kev-pro.example
Nice to have
• Variations of the colors scheme of a redish-orange (C:0,M:84,Y:100,K:0), grey, white, black. Logo, card, or text can be in any of these colors.
• Possible quote like "Take control of your personal health to unleash your greatest potential" or "Unleashing your greatness first begins with fitness of the body and mind"

```html
<!DOCTYPE html>
<html lang="en">
<head>
<meta charset="utf-8">
<title>Darren Holcombe Fitness — Business Card</title>
<link rel="stylesheet" href="https://fonts.googleapis.com/css2?family=Oswald:wght@300;400;500;700&display=swap">
<style>
  :root {
    --brand-orange: #f05428;
    --ink: #000000;
    --paper: #ffffff;
  }
  html, body {
    margin: 0;
    padding: 0;
    overflow: hidden;
    background: var(--paper);
  }
  .card {
    position: relative;
    width: 686px;
    height: 1200px;
    background: var(--paper);
    overflow: hidden;
    font-family: "Oswald", sans-serif;
    color: var(--ink);
  }
  .quote-mark {
    position: absolute;
    left: 59px;
    top: 522px;
    width: 84px;
    height: 82px;
  }
  .quote-mark path { fill: var(--brand-orange); }
  .quote-text {
    position: absolute;
    left: 73px;
    top: 588px;
    margin: 0;
    font-size: 27px;
    font-weight: 400;
    line-height: 34px;
    letter-spacing: -0.2px;
  }
  .owner-name {
    position: absolute;
    left: 58px;
    top: 811px;
    margin: 0;
    font-size: 80px;
    font-weight: 500;
    line-height: 1;
    letter-spacing: -1px;
    white-space: nowrap;
  }
  .owner-name .initial { color: var(--brand-orange); }
  .company-name {
    position: absolute;
    left: 59px;
    top: 908px;
    margin: 0;
    font-size: 20px;
    font-weight: 400;
    line-height: 1;
    letter-spacing: 6.3px;
    text-transform: uppercase;
    color: var(--brand-orange);
    white-space: nowrap;
  }
  .divider {
    position: absolute;
    left: 59px;
    top: 981px;
    width: 27px;
    height: 6px;
    background: var(--brand-orange);
  }
  .contact {
    position: absolute;
    left: 59px;
    top: 1002px;
    margin: 0;
    font-style: normal;
    font-size: 27px;
    font-weight: 300;
    line-height: 34px;
    letter-spacing: -0.3px;
  }
  .contact span { display: block; }
</style>
</head>
<body>
  <main class="card">
    <svg class="quote-mark" viewBox="0 0 84 82" aria-hidden="true">
      <path d="M0 42 Q0 6 32 0 L36 11 Q21 17 20 32 L36 32 L36 82 L0 82 Z"/>
      <path d="M46 42 Q46 6 78 0 L82 11 Q67 17 66 32 L82 32 L82 82 L46 82 Z"/>
    </svg>
    <p class="quote-text">Take control of your personal health to unleash<br>your greatest potential.</p>

    <h1 class="owner-name"><span class="initial">D</span>arren <span class="initial">H</span>olcombe</h1>
    <p class="company-name">Darren Holcombe Fitness</p>

    <div class="divider"></div>

    <address class="contact">
      <span class="contact-email">dan@kev-pro.example</span>
      <span class="contact-web">www.kev-pro.example</span>
    </address>
  </main>
</body>
</html>
```